Parks Dept. Ad for Outside Exercise

We need a design for a 1/3 page ad in a regional fitness magazine. I got the initial design from one of our staffers at the parks dept. and knew we should/could find someone, and spend a little money to do better. I've uploaded the initial design to help with understanding the idea of what we're looking for, but feel free to go in a different direction. Obviously, less text! And I don't know why it has it twice...

Target Market(s)

people interested in fitness magazines

Industry/Entity Type

Fitness

Requirements
Must have
• must provide a sense of why outdoor exercise is desirable and that the city of Riverbend provides those benefits with our wonderful park system. Logo of the city (White or blue) and Parks and Rec contact info must be in ad, though certainly not as prominent as they had displayed in the initial ad.

```html
<!DOCTYPE html>
<html lang="en">
<head>
<meta charset="utf-8">
<title>Benefits of Exercising in Nature – Riverbend Parks and Recreation</title>
<link rel="stylesheet" href="https://fonts.googleapis.com/css2?family=Londrina+Solid:wght@400&family=Kaushan+Script&family=Boogaloo&family=Source+Sans+3:wght@400;700&display=swap">
<style>
  :root {
    --forest-deep: #1f5a1a;
    --forest: #3f8f2a;
    --leaf: #8cc63f;
    --path: #c9d3c2;
    --ink-white: #ffffff;
    --shadow: rgba(20, 40, 15, 0.75);
    --brand-blue: #1565c0;
    --contact-ink: #1a2a1a;
  }
  html, body {
    margin: 0;
    padding: 0;
    width: 1195px;
    height: 1200px;
    overflow: hidden;
    background: var(--forest-deep);
  }
  .ad {
    position: relative;
    width: 1195px;
    height: 1200px;
    overflow: hidden;
    font-family: "Boogaloo", sans-serif;
    color: var(--ink-white);
  }
  .trail-scene {
    position: absolute;
    inset: 0;
    background:
      radial-gradient(ellipse 45% 30% at 55% 72%, var(--path) 0%, rgba(201,211,194,0) 100%),
      radial-gradient(ellipse 40% 35% at 72% 35%, #c6e56a 0%, rgba(198,229,106,0) 100%),
      radial-gradient(ellipse 70% 65% at 50% 50%, var(--leaf) 0%, var(--forest) 70%, var(--forest-deep) 100%);
  }
  .frame {
    position: absolute;
    inset: 0;
    border: 4px solid var(--forest);
    pointer-events: none;
  }
  .headline {
    position: absolute;
    inset: 0;
    width: 1195px;
    height: 1200px;
  }
  .headline text {
    fill: var(--ink-white);
    filter: drop-shadow(4px 4px 2px rgba(20, 40, 15, 0.75));
  }
  .headline .script { font-family: "Kaushan Script", cursive; }
  .headline .block { font-family: "Londrina Solid", sans-serif; }

  .benefit-list {
    margin: 0;
    padding: 0;
    list-style: none;
    font-size: 48px;
    line-height: 56px;
    text-shadow: 3px 3px 0 var(--shadow);
  }
  .benefit-list li {
    position: absolute;
    left: 118px;
    padding-left: 58px;
    white-space: nowrap;
  }
  .benefit-list .bullet {
    position: absolute; left: 0; top: 12px; width: 38px; height: 34px;
  }
  .benefit-focus { top: 580px; }
  .benefit-creativity { top: 664px; }
  .benefit-stress { top: 748px; }
  .benefit-oxygen { top: 832px; }

  .park-tagline {
    position: absolute;
    left: 702px;
    top: 800px;
    margin: 0;
    font-size: 36px;
    line-height: 42px;
    text-shadow: 3px 3px 0 var(--shadow);
  }

  .org-signoff {
    position: absolute;
    left: 702px;
    top: 912px;
    font-family: "Source Sans 3", sans-serif;
    color: var(--contact-ink);
  }
  .org-mark {
    display: flex; align-items: center; gap: 10px;
    font-family: "Source Sans 3", sans-serif;
    font-weight: 700;
    font-size: 34px; color: var(--brand-blue);
    margin-bottom: 12px;
  }
  .org-mark .dot { width: 26px; height: 26px; border-radius: 50%; background: var(--brand-blue); }
  .org-name { font-weight: 700; font-size: 21px; margin: 0 0 6px; }
  .org-contact { font-size: 19px; margin: 0 0 6px; }
</style>
</head>
<body>
<main class="ad">
  <div class="trail-scene" role="img" aria-label="Photo of two people walking along a shaded paved park trail lined with green trees"></div>

  <svg class="headline" viewBox="0 0 1195 1200" role="heading" aria-level="1" aria-label="Benefits of exercising in nature">
    <text class="script" x="38" y="160" font-size="150" textLength="478" lengthAdjust="spacingAndGlyphs">benefits</text>
    <text class="script" x="540" y="162" font-size="96">of</text>
    <text class="block" x="54" y="306" font-size="118" textLength="1068" lengthAdjust="spacingAndGlyphs">EXERCISING</text>
    <text class="script" x="42" y="450" font-size="110">in</text>
    <text class="block" x="186" y="516" font-size="232" textLength="924" lengthAdjust="spacingAndGlyphs">NATURE</text>
    <text class="block" x="174" y="1098" font-size="100" textLength="438" lengthAdjust="spacingAndGlyphs">OXYGEN</text>
  </svg>

  <ul class="benefit-list">
    <li class="benefit-focus"><svg class="bullet" viewBox="0 0 38 34" aria-hidden="true"><path d="M19 32 L4 17 A9 9 0 0 1 19 6 A9 9 0 0 1 34 17 Z" fill="none" stroke="#fff" stroke-width="4"/></svg>Sharper focus</li>
    <li class="benefit-creativity"><svg class="bullet" viewBox="0 0 38 34" aria-hidden="true"><path d="M19 32 L4 17 A9 9 0 0 1 19 6 A9 9 0 0 1 34 17 Z" fill="none" stroke="#fff" stroke-width="4"/></svg>More creativity</li>
    <li class="benefit-stress"><svg class="bullet" viewBox="0 0 38 34" aria-hidden="true"><path d="M19 32 L4 17 A9 9 0 0 1 19 6 A9 9 0 0 1 34 17 Z" fill="none" stroke="#fff" stroke-width="4"/></svg>Less stress</li>
    <li class="benefit-oxygen"><svg class="bullet" viewBox="0 0 38 34" aria-hidden="true"><path d="M19 32 L4 17 A9 9 0 0 1 19 6 A9 9 0 0 1 34 17 Z" fill="none" stroke="#fff" stroke-width="4"/></svg>Breathe in more</li>
  </ul>

  <p class="park-tagline">Find it all on Riverbend's<br>park trails</p>

  <footer class="org-signoff">
    <div class="org-mark"><span class="dot"></span>Riverbend</div>
    <p class="org-name">Riverbend Parks and Recreation</p>
    <p class="org-contact">riverbendparks.org &nbsp;•&nbsp; 555-014-2290</p>
    <p class="org-contact">parks@riverbend.gov</p>
  </footer>

  <div class="frame"></div>
</main>
</body>
</html>
```